Facebook & Instagram Ads for Velvet Drift, the world's first device to improve memory throu...

About Us
Velvet Drift® is a revolutionary bedside device that improves memory while you sleep. Backed by groundbreaking clinical research from the Norbrook State University Halvern, our device uses gentle, rotating scents to enhance memory and brian fog naturally. With zero pills, zero side effects, and zero effort, Velvet Drift offers a new path to better memory. www.velvetdrift-example.com

The Challenge
We are looking for bold, imaginative, and highly shareable static and GIF ad designs for Facebook and Instagram. This isn’t just another health device—it’s a category-defining product. Your job is to help us stop the scroll with creative ad concepts that communicate the elegance, science, and life-changing benefits of Velvet Drift.

What We’re Looking For
Format: Static images + short GIF animations (3–8 seconds)
Platforms: Facebook feed, Instagram feed, Instagram Reels
Style: Modern, aspirational, elegant, clean — with a premium feel
Target Audience: Affluent men and women, ages 50+, health-conscious, looking for ways to support memory and brain health and people concerned or worried that they’re losing their memory and aren’t thinking as quickly or crisply as they want,

Creative Direction
Show Velvet Drift as a premium lifestyle product (not medical or clinical in look).
Think high-end wellness meets cutting-edge science.
Use strong visual hooks: elegant bedside setups, active seniors, subtle cues to scents and sleep, calming colors.
Text overlays should be minimal and impactful.

Tone of Voice (for ad copy in the designs)
Aspirational yet credible
Warm, trustworthy, and empowering
Avoid fear tactics or overpromising

Approved Messaging
✅ Velvet Drift improves memory while you sleep
✅ Clinically backed & drug-free
✅ Simple, effortless nightly use
✅ No RX, no side effects
✅ Elegant bedside design
✅ Improves your mood
✅ Feel Younger
✅ Developed by a top 2% scientist in the world (Caldermoor School of Medicine Study)
✅ 226% memory improvement in seniors
✅ 300% memory improvement in dementia patients

Do NOT Say
❌ Cures Alzheimer’s or dementia
❌ Guaranteed results
❌ Any medical claims beyond memory improvement and cognition support

Deliverables
2+ static ad concepts (1080x1080 + 1080x1920 formats)
1+ short GIF ad concepts (3–8 seconds, loopable)
Layered source files (PSD/AI) preferred

What We’ll Provide You
Our website for reference: www.velvetdrift-example.com
Brand guidelines (logo, colors, fonts)
Approved copy lines and scientific references
Device imagery (with logo placement guidelines)

What We Want to See in Your Work
Unique and scroll-stopping ad ideas (not cookie-cutter templates)
Clever ways to communicate memory improvement + science through visuals
A mix of direct product focus AND lifestyle storytelling

Inspiration
Think of Quillo, Tesvi Band, or Brantel level of sleekness—premium, modern, aspirational.

⚡ Your mission: Help us tell the world about the first device that can improve memory while you sleep—with ads so compelling people can’t scroll past.

```html
<!DOCTYPE html>
<html lang="en">
<head>
<meta charset="utf-8">
<title>Velvet Drift – Social Ads</title>
<link rel="stylesheet" href="https://fonts.googleapis.com/css2?family=Montserrat:wght@300;400;500;700;800&display=swap">
<style>
  :root{
    --stage:#5a5a5a;
    --sky-top:#3f6d92;
    --sky-mid:#8fb2c8;
    --sky-light:#c9d8de;
    --snow:#eeeeee;
    --paper:#e4e4e2;
    --ink:#1d1d1d;
    --brown:#3a2a22;
    --band:#2a1a12;
    --line:#2e2520;
    --device:#ececea;
    --device-shade:#d6d5d2;
    --copper:#c8683a;
    --white:#ffffff;
  }
  *{margin:0;padding:0;box-sizing:border-box}
  html,body{width:1200px;height:624px;overflow:hidden;background:var(--stage);font-family:"Montserrat",sans-serif}
  .canvas{position:relative;width:1200px;height:624px}
  .ad{position:absolute;top:42px;width:540px;height:540px;overflow:hidden}
  .ad--dream{left:36px}
  .ad--product{left:626px;background:var(--paper)}

  /* Dream ad */
  .dream-scene{position:absolute;inset:0;background:radial-gradient(ellipse at 55% 45%,var(--sky-light) 0%,var(--sky-mid) 45%,var(--sky-top) 100%)}
  .dream-frame{position:absolute;left:12px;top:12px;width:516px;height:440px;border:2px solid var(--white);border-bottom:none}
  .snow{position:absolute;left:0;bottom:0;width:540px;height:110px}
  .brand-name{position:absolute;color:var(--ink);font-weight:500;text-align:center;letter-spacing:1px;line-height:1}
  .ad--dream .brand-name{left:0;width:540px;top:52px;font-size:42px}
  .device-left{position:absolute;left:367px;top:300px;width:150px;height:226px;border-radius:10px;
    background:linear-gradient(90deg,var(--device) 0%,var(--white) 45%,var(--device-shade) 100%)}
  .claim{position:absolute;left:32px;top:440px;color:var(--brown)}
  .claim__light{font-size:26px;font-weight:300;line-height:1.2;color:var(--ink)}
  .claim__bold{font-size:27px;font-weight:700;line-height:1.2}

  /* Product ad */
  .frame-line{position:absolute;background:var(--line)}
  .frame-line--top{left:30px;top:33px;width:300px;height:2px}
  .frame-line--left{left:30px;top:33px;width:2px;height:340px}
  .frame-line--right{left:508px;top:132px;width:2px;height:241px}
  .hatch-disc{position:absolute;left:137px;top:58px;width:104px;height:104px;border-radius:50%;background:#c4c3c0;opacity:.7}
  .ad--product .brand-name{left:381px;top:18px;width:136px;font-size:24px;line-height:1.1}
  .plinth-outline{position:absolute;left:125px;top:322px;width:290px;height:68px;border:6px solid var(--line);border-bottom:none}
  .plinth-block{position:absolute;left:148px;top:346px;width:242px;height:44px;background:var(--band)}
  .band{position:absolute;left:0;top:373px;width:540px;height:134px;background:var(--band)}
  .device-right{position:absolute;left:192px;top:102px;width:156px;height:290px;border-radius:8px;
    background:linear-gradient(90deg,var(--device-shade) 0%,var(--device) 40%,var(--white) 60%,var(--device-shade) 100%)}
  .headline{position:absolute;left:0;width:540px;top:420px;text-align:center;color:var(--white)}
  .headline__intro{font-size:22px;font-weight:400;line-height:1.2}
  .headline__main{font-size:27px;font-weight:800;line-height:1.5;letter-spacing:.5px}
</style>
</head>
<body>
<main class="canvas">

  <section class="ad ad--dream">
    <div class="dream-scene" role="img" aria-label="Woman sleeping peacefully on a soft cloud in a blue sky"></div>
    <div class="dream-frame"></div>
    <svg class="snow" viewBox="0 0 540 110" role="img" aria-label="Soft white cloud texture along the bottom" preserveAspectRatio="none">
      <path d="M0 22 L40 12 L80 18 L120 6 L160 14 L200 4 L240 10 L280 6 L320 14 L360 12 L400 18 L440 10 L480 16 L540 8 L540 110 L0 110 Z" fill="var(--snow)"/>
    </svg>
    <div class="brand-name">Velvet Drift</div>
    <div class="device-left" role="img" aria-label="White Velvet Drift bedside device with copper trim"></div>
    <div class="claim">
      <p class="claim__light">Clinically</p>
      <p class="claim__bold">Backed &amp; Drug-Free</p>
    </div>
  </section>

  <section class="ad ad--product">
    <div class="frame-line frame-line--top"></div>
    <div class="frame-line frame-line--left"></div>
    <div class="frame-line frame-line--right"></div>
    <div class="hatch-disc" role="img" aria-label="Decorative line-textured circle"></div>
    <div class="brand-name">Velvet Drift</div>
    <div class="band"></div>
    <div class="plinth-outline"></div>
    <div class="plinth-block"></div>
    <div class="device-right" role="img" aria-label="White Velvet Drift device with front fan grille and copper trim"></div>
    <div class="headline">
      <p class="headline__intro">Velvet Drift Improves</p>
      <p class="headline__main">MEMORY WHILE YOU SLEEP</p>
    </div>
  </section>

</main>
</body>
</html>
```